Logo and Business card design!

Welbrook Estates

We are a Property development and real estate company (needs a logo design).

Welbrook estates is based in Sydney Australia and will be dealing with high net worth individuals with a corporate background. The demographic of clients will be relatively youthful and savvy. We do development finance, property development and some portion of property sales

I'd like the 'Welbrook' part of the name to be strength of the title, with 'property' playing a very minor part, perhaps in tiny font somewhere off to the bottom or side or something

Thank you!

Target Market(s)

25-55 years old

Industry/Entity Type

Real Estate Development

Contact Information for Business Card

Please arrange this information as you see fit

Leon Brightwater
Managing Director
0417 582 273
leon@welbrookestates-example.com.au
www.welbrookestates-example.com.au

Logo Text

Welbrook estates

Font styles to use
Serif

Colors

Designer to choose colors to be used in the design.

Requirements
Must have
• PLEASE VIEW THE UPLOADED IMAGES AND EXAMPLES
• And please put 'property' in small letters at the bottom or to the side. I want it to play a minimalist role, with 'WELBROOK' being the feature
• Colours! Please make sure theyre mostly grey and white with possibly some other dark blue and maybe dark grey
Nice to have
• Please feel free to use whatever colors you like, the suggested colors are something I selected momentarily and dont necessarily reflect strict guidelines
Should not have
• NO pictures or shapes of houses. I dont want the logo design to be so literal in its imagery

```html
<!DOCTYPE html>
<html lang="en">
<head>
<meta charset="utf-8">
<title>Welbrook Estates — Identity and Business Card</title>
<link rel="stylesheet" href="https://fonts.googleapis.com/css2?family=Arimo:wght@400;700&display=swap">
<style>
  :root {
    --blue: #1f6fb8;
    --blue-deep: #0d4f9e;
    --blue-light: #2a7cc0;
    --ink: #1e2a36;
    --grey: #6b6f74;
    --silver: #d6dbe0;
    --paper: #ffffff;
    --page: #ffffff;
  }
  * { box-sizing: border-box; margin: 0; padding: 0; }
  html, body { width: 1200px; height: 1200px; overflow: hidden; }
  body {
    background: var(--page);
    font-family: "Arimo", Arial, sans-serif;
    position: relative;
  }

  /* Primary wordmark */
  .brand-lockup {
    position: absolute;
    top: 230px;
    left: 50%;
    transform: translateX(-50%);
    display: flex;
    align-items: center;
    gap: 22px;
    color: var(--blue-deep);
  }
  .brand-square {
    width: 70px; height: 70px;
    background: var(--blue-deep);
  }
  .brand-name { display: flex; flex-direction: column; font-weight: 400; }
  .brand-name .main { font-size: 64px; letter-spacing: 6px; line-height: 1; }
  .brand-name .sub { font-size: 16px; letter-spacing: 18px; margin-top: 10px; }

  /* Cards */
  .card {
    position: absolute;
    top: 560px;
    width: 540px;
    height: 320px;
    overflow: hidden;
    box-shadow: 0 6px 18px rgba(20, 40, 70, 0.18);
  }
  .card-front { left: 40px; background: var(--blue); }
  .card-back {
    left: 620px;
    background: linear-gradient(135deg, var(--blue-light) 0%, var(--blue-deep) 100%);
    display: flex; align-items: center; justify-content: center;
  }

  .front-face {
    position: absolute; inset: 0;
    background: var(--paper);
    clip-path: polygon(120px 14px, 100% 14px, 100% 100%, 190px 100%, 190px 150px, 0 150px, 0 74px, 104px 74px, 120px 58px);
  }

  .front-logo {
    position: absolute; left: 14px; top: 90px;
    display: flex; align-items: center; gap: 8px;
    color: var(--blue-deep);
  }
  .front-logo .mark { width: 22px; height: 22px; background: var(--blue-deep); }
  .front-logo .name { display: flex; flex-direction: column; }
  .front-logo .name .main { font-size: 19px; letter-spacing: 1.5px; line-height: 1; }
  .front-logo .name .sub { font-size: 7px; letter-spacing: 5px; margin-top: 3px; }

  .side-url {
    position: absolute;
    left: 172px; top: 160px;
    transform-origin: left top;
    transform: rotate(90deg);
    color: var(--paper);
    font-size: 8px;
    line-height: 1;
    letter-spacing: 0.2px;
    white-space: nowrap;
  }

  .phone {
    position: absolute; right: 26px; top: 34px;
    color: var(--blue); font-size: 24px; letter-spacing: 1px;
  }
  .contact {
    position: absolute; left: 214px; top: 168px;
    text-transform: uppercase;
  }
  .contact .person { color: var(--blue-deep); font-size: 26px; letter-spacing: 1px; }
  .contact .role { color: var(--ink); font-size: 16px; letter-spacing: 1.5px; margin-top: 4px; }
  .contact .line { color: var(--ink); font-size: 10px; letter-spacing: 0.6px; margin-top: 10px; }
  .contact .line + .line { margin-top: 4px; }

  .back-logo { display: flex; align-items: center; gap: 14px; color: var(--silver); }
  .back-logo .mark { width: 40px; height: 40px; background: var(--silver); }
  .back-logo .name { display: flex; flex-direction: column; }
  .back-logo .name .main { font-size: 34px; letter-spacing: 3px; line-height: 1; }
  .back-logo .name .sub { font-size: 10px; letter-spacing: 10px; margin-top: 6px; }
</style>
</head>
<body>

  <div class="brand-lockup">
    <div class="brand-square"></div>
    <div class="brand-name">
      <span class="main">WELBROOK</span>
      <span class="sub">ESTATES</span>
    </div>
  </div>

  <section class="card card-front" aria-label="Business card front">
    <div class="front-face"></div>
    <div class="front-logo">
      <div class="mark"></div>
      <div class="name">
        <span class="main">WELBROOK</span>
        <span class="sub">ESTATES</span>
      </div>
    </div>
    <div class="side-url">www.welbrookestates-example.com.au</div>
    <div class="phone">0417 582 273</div>
    <div class="contact">
      <p class="person">Leon Brightwater</p>
      <p class="role">Managing Director</p>
      <p class="line">leon@welbrookestates-example.com.au</p>
      <p class="line">www.welbrookestates-example.com.au</p>
    </div>
  </section>

  <section class="card card-back" aria-label="Business card back">
    <div class="back-logo">
      <div class="mark"></div>
      <div class="name">
        <span class="main">WELBROOK</span>
        <span class="sub">ESTATES</span>
      </div>
    </div>
  </section>

</body>
</html>
```